Business Card Design

Cake decorating business in a small town in Australia. looking for a style that is fresh with a touch of vintage/country. liking these ideas, timber backgrounds, chalkboards, bunting, flowers and cake elements (rolling pins, cupcakes, cake stands, etc.) would consider a shot saying/statement. would like the back of the card to have wording "Specialising in delectable treats for all your special occasions" - wedding cakes - birthday cakes - special occasion cakes - novelty cakes - cupcakes, cookies, slices and cake pops. maybe incorporate a cake in design on back page. attached are a few of my favourite cakes and the start of a card design I liked.

Industry/Entity Type

Business

Contact Information for Business Card

Marigold's Sugarloft Bakes 0438 056 969Find me on (Chirpwall Logo)

Requirements
Nice to have
• timber, some of my designs, chalkboard, baking utensils
Should not have
• no red font

```html
<!DOCTYPE html>
<html lang="en">
<head>
<meta charset="utf-8">
<title>Marigold's Sugarloft Bakes — Business Card</title>
<link rel="stylesheet" href="https://fonts.googleapis.com/css2?family=Dancing+Script:wght@500;700&family=Parisienne&display=swap">
<style>
  :root {
    --canvas: #e9e6e3;
    --timber-light: #8a7660;
    --timber-mid: #6b5846;
    --timber-dark: #4a3c30;
    --chalk: #3a3836;
    --chalk-line: #a08a66;
    --pink: #f4b6c6;
    --pink-soft: #f7d3dc;
    --cream: #f2ece4;
    --ink: #2b2523;
    --band: rgba(255, 255, 255, 0.78);
  }
  * { box-sizing: border-box; margin: 0; padding: 0; }
  html, body { width: 1200px; height: 800px; overflow: hidden; }
  body {
    background: var(--canvas);
    display: flex;
    align-items: center;
    justify-content: center;
    gap: 40px;
  }
  .card {
    position: relative;
    width: 540px;
    height: 310px;
    border-radius: 18px;
    overflow: hidden;
    box-shadow: 0 10px 28px rgba(0, 0, 0, 0.22);
  }

  /* Front */
  .card-front .timber {
    position: absolute; inset: 0;
    background: linear-gradient(160deg, var(--timber-light), var(--timber-mid) 55%, var(--timber-dark));
  }
  .card-front .frame { position: absolute; inset: 0; }
  .cake-art {
    position: absolute;
    left: 22px; top: 98px;
    width: 100px; height: 170px;
    border-radius: 10px 10px 4px 4px;
    background: linear-gradient(180deg, var(--pink-soft), var(--pink));
  }
  .brand-name {
    position: absolute;
    left: 150px; right: 30px; top: 46px;
    text-align: center;
    font-family: "Dancing Script", cursive;
    font-weight: 700;
    font-size: 40px;
    line-height: 1.1;
    color: var(--pink);
  }
  .services {
    position: absolute;
    left: 148px; right: 34px; top: 128px;
    text-align: center;
    font-family: "Dancing Script", cursive;
    font-weight: 500;
    font-size: 19px;
    line-height: 1.35;
    color: var(--cream);
  }
  .phone {
    position: absolute;
    left: 232px; top: 204px;
    width: 156px; height: 24px;
    border-radius: 12px;
    background: var(--pink);
    color: var(--ink);
    font-family: "Dancing Script", cursive;
    font-weight: 700;
    font-size: 16px;
    line-height: 24px;
    text-align: center;
  }

  /* Back */
  .card-back .cake-photo {
    position: absolute; inset: 0;
    background:
      radial-gradient(circle at 68% 42%, #fdf3f1 0 17%, #f6cfd3 27%, rgba(246, 207, 211, 0) 40%),
      linear-gradient(180deg, var(--timber-mid) 0 30%, rgba(0,0,0,0) 30%),
      linear-gradient(90deg, #d7a3b2, #e6b7c3 60%, var(--timber-dark));
  }
  .tagline-band {
    position: absolute;
    left: 0; right: 0; top: 170px;
    height: 36px;
    background: var(--band);
    display: flex;
    align-items: center;
    justify-content: center;
  }
  .tagline {
    font-family: "Parisienne", cursive;
    font-size: 19px;
    color: var(--ink);
    letter-spacing: 0.5px;
  }
</style>
</head>
<body>

  <section class="card card-front" aria-label="Business card front">
    <div class="timber" role="img" aria-label="Rustic timber plank background"></div>
    <svg class="frame" width="540" height="310" viewBox="0 0 540 310" aria-hidden="true">
      <path d="M95 36 H485 A36 36 0 0 0 521 72 V238 A36 36 0 0 0 485 274 H95 A36 36 0 0 0 59 238 V72 A36 36 0 0 0 95 36 Z"
            fill="var(--chalk)"/>
      <path d="M100 46 H480 A34 34 0 0 0 511 77 V233 A34 34 0 0 0 480 264 H100 A34 34 0 0 0 69 233 V77 A34 34 0 0 0 100 46 Z"
            fill="none" stroke="var(--chalk-line)" stroke-width="1.5"/>
    </svg>
    <div class="cake-art" role="img" aria-label="Pink tiered cake on a stand with candles"></div>
    <h1 class="brand-name">Marigold's Sugarloft Bakes</h1>
    <p class="services">wedding cakes - birthday cakes - novelty cakes<br>cupcakes - cookies slices and cake pops</p>
    <p class="phone">0417 382 254</p>
  </section>

  <section class="card card-back" aria-label="Business card back">
    <div class="cake-photo" role="img" aria-label="Pink iced cake topped with a large pale pink sugar flower on timber"></div>
    <div class="tagline-band">
      <p class="tagline">Specialising in delectable treats for all your special occasions</p>
    </div>
  </section>

</body>
</html>
```